Business Card Design

I am a GP with interest in Dermatology and Aesthetic Medicin, performing Botulinum Toxin Type A and Dermal Fillers treatmets in Cosmetic Dermatology clinic.

I am looking for a white colour, good quality white paper card may be of some special texture with black calligraphic writing but easy to read and not to wiggly- professional- looking.

Really appreciate your help.

Milena

Contact Information for Business Card

Cosmetic Dermatology Clinic

Dr Milena Ravitskaya, MBBS, MRCGP, DPD

Tel: 07915 462 170
milena@medpractice-mail.co.uk

```html
<!DOCTYPE html>
<html lang="en">
<head>
<meta charset="utf-8">
<title>Cosmetic Dermatology Clinic – Business Card</title>
<link rel="stylesheet" href="https://fonts.googleapis.com/css2?family=Jost:wght@400&family=Oswald:wght@500&family=Exo+2:ital,wght@0,400;1,400&display=swap">
<style>
  :root {
    --page: #e9e9ea;
    --card: #ffffff;
    --ink: #1e1e1e;
    --ink-soft: #3a3a3a;
    --silver-light: #f4f4f4;
    --silver-mid: #cfcfcf;
    --silver-dark: #8a8a8a;
    --tab: #232323;
  }
  * { box-sizing: border-box; margin: 0; padding: 0; }
  html, body {
    width: 1200px; height: 877px; overflow: hidden;
    background: var(--page);
  }
  .sheet {
    position: relative; width: 1200px; height: 877px;
    display: flex; align-items: center; justify-content: center; gap: 40px;
  }
  .card {
    position: relative; width: 540px; height: 309px;
    background: linear-gradient(160deg, var(--card) 0%, #f7f7f7 100%);
    box-shadow: 0 6px 22px rgba(0,0,0,.16);
    overflow: hidden;
    color: var(--ink);
  }
  .clinic-name {
    position: absolute; font-family: "Jost", sans-serif; font-weight: 400;
    color: var(--ink-soft); white-space: nowrap;
  }

  /* back face */
  .card-back .clinic-name { left: 34px; top: 30px; font-size: 29px; }
  .card-back .pill { position: absolute; left: 22px; top: 92px; }
  .card-back .rules { position: absolute; left: 0; top: 222px; }

  /* front face */
  .card-front .clinic-name { left: 26px; top: 22px; font-size: 33px; }
  .tab { position: absolute; width: 38px; height: 38px; background: var(--tab); border-radius: 5px; }
  .tab-left { left: -6px; top: 82px; }
  .tab-right { right: -6px; top: 132px; }
  .person { position: absolute; left: 0; right: 0; top: 92px; text-align: center; }
  .person-name {
    display: inline-block;
    font-family: "Oswald", sans-serif; font-weight: 500; font-size: 29px;
    letter-spacing: .5px; line-height: 1; transform: scaleX(.86); transform-origin: center;
    white-space: nowrap;
  }
  .person-role {
    font-family: "Exo 2", sans-serif; font-size: 9px; letter-spacing: 1.2px; margin-top: 3px;
  }
  .address {
    position: absolute; left: 40px; width: 452px; top: 162px; text-align: center;
    font-family: "Exo 2", sans-serif; font-style: italic; font-size: 12.5px; white-space: nowrap;
  }
  .address-rule { position: absolute; left: 40px; top: 180px; width: 452px; height: 2px; background: var(--ink); }
  .divider { position: absolute; left: 240px; top: 200px; width: 1.5px; height: 62px; background: var(--ink); }
  .contact {
    position: absolute; display: flex; align-items: center; gap: 9px;
    font-family: "Exo 2", sans-serif; font-size: 12.5px; color: var(--ink); white-space: nowrap;
  }
  .contact svg { flex: none; }
  .phone-1 { left: 40px; top: 196px; }
  .phone-2 { left: 40px; top: 234px; }
  .email { left: 268px; top: 205px; font-size: 12px; }
  .website { left: 268px; top: 240px; font-size: 12px; }
</style>
</head>
<body>
<main class="sheet">

  <section class="card card-back" aria-label="Card back">
    <h2 class="clinic-name">Cosmetic Dermatology Clinic</h2>
    <svg class="pill" width="300" height="86" viewBox="0 0 300 86">
      <defs>
        <linearGradient id="pillFill" x1="0" y1="0" x2="1" y2="1">
          <stop offset="0" stop-color="#f4f4f4"/>
          <stop offset=".5" stop-color="#cfcfcf"/>
          <stop offset="1" stop-color="#ededed"/>
        </linearGradient>
      </defs>
      <path d="M42 4 H290 V82 H42 A39 39 0 0 1 42 4 Z" fill="url(#pillFill)" stroke="#2a2a2a" stroke-width="2.5"/>
    </svg>
    <svg class="rules" width="540" height="50" viewBox="0 0 540 50">
      <defs>
        <linearGradient id="ruleFill" x1="0" x2="1">
          <stop offset="0" stop-color="#8a8a8a"/>
          <stop offset=".45" stop-color="#f4f4f4"/>
          <stop offset="1" stop-color="#8a8a8a"/>
        </linearGradient>
      </defs>
      <rect x="0" y="4" width="540" height="5" fill="url(#ruleFill)"/>
      <rect x="0" y="32" width="540" height="5" fill="url(#ruleFill)"/>
    </svg>
  </section>

  <section class="card card-front" aria-label="Card front">
    <h1 class="clinic-name">Cosmetic Dermatology Clinic</h1>
    <span class="tab tab-left"></span>
    <span class="tab tab-right"></span>

    <div class="person">
      <p class="person-name">MILENA RAVITSKAYA</p>
      <p class="person-role">GENERAL MANAGER</p>
    </div>

    <p class="address">42 Harwood Lane, 2nd Floor, Kestrel Street</p>
    <span class="address-rule"></span>
    <span class="divider"></span>

    <p class="contact phone-1">
      <svg width="20" height="20" viewBox="0 0 20 20"><circle cx="10" cy="10" r="8.5" fill="none" stroke="currentColor" stroke-width="1.3"/><path d="M7 5.5 L8.6 7.6 L7.7 8.8 Q8.8 11.4 11.2 12.4 L12.4 11.4 L14.5 13 L13.3 14.6 Q8.6 14.4 5.6 7 Z" fill="currentColor"/></svg>
      07915 462 170
    </p>
    <p class="contact phone-2">
      <svg width="20" height="20" viewBox="0 0 20 20"><circle cx="10" cy="10" r="8.5" fill="none" stroke="currentColor" stroke-width="1.3"/><rect x="7" y="4.5" width="6" height="11" rx="1" fill="none" stroke="currentColor" stroke-width="1.3"/><circle cx="10" cy="13.4" r=".8" fill="currentColor"/></svg>
      020 7946 0183
    </p>
    <p class="contact email">
      <svg width="20" height="20" viewBox="0 0 20 20"><circle cx="10" cy="10" r="9" fill="currentColor"/><rect x="5" y="6.5" width="10" height="7" fill="#fff"/><path d="M5 6.5 L10 10.5 L15 6.5" fill="none" stroke="currentColor" stroke-width="1.1"/></svg>
      milena@medpractice-mail.co.uk
    </p>
    <p class="contact website">
      <svg width="20" height="20" viewBox="0 0 20 20"><circle cx="10" cy="10" r="9" fill="currentColor"/><g fill="none" stroke="#fff" stroke-width="1"><circle cx="10" cy="10" r="5.5"/><ellipse cx="10" cy="10" rx="2.3" ry="5.5"/><path d="M4.5 10 H15.5 M5.5 7 H14.5 M5.5 13 H14.5"/></g></svg>
      www.cdclinic-care.co.uk
    </p>
  </section>

</main>
</body>
</html>
```